Business Card Design Project (Beer industry)

I am seeking a redesign of my business card. I am looking for something that will really stand out in both texture and feel. Something more on the modern side then traditional. Nothing die cut shaped like a beer mug please.

The card is used mostly for other industry professionals, as well as bar and restaurant owners. My title is Strategy & Acquisitions. If you would like to somehow incorporate that theme, that may work.

My business is craft and imported beer. Nothing fizzy and yellow, so my products are more on the upscale side.
Updates

I was able to update my logo in .ai and .tif format. I hope that helps. 

Thank you all for your creative ideas. I have uploaded my current business card in pdf format, as well as our logo in .eps file format. We are excited about the submissions so far and want to thank you all again.

PS Please do not include fax number in future submissions, as we are looking for something more creative and a fax says 1999 and not 2015, which is the message we are going for, without being futuristic. 

Thank you all once again for all of your submissions. If we would consider a two sided card, we would like the opposite side not to be the same as the front. The styles we have seen so far, it appears the front and back are too similar. Again, a two sided card is not required. Thank you and we look forward to pushing the boundaries of your creativity. Cheers

Target Market(s)

My card would mostly go to bar and restaurant operators as well as other beer industry professionals

Industry/Entity Type

Restaurant

Requirements
Nice to have
• Two sided would be considered, although not required
Should not have
• Anything die cut shaped like a beer mug.

```html
<!DOCTYPE html>
<html lang="en">
<head>
<meta charset="utf-8">
<title>Harbor Tap Co. – Business Card</title>
<link rel="stylesheet" href="https://fonts.googleapis.com/css2?family=Arimo:wght@400;700&display=swap">
<style>
  :root {
    --stage: #000000;
    --brand-red: #97131f;
    --paper: #ffffff;
    --ink: #4a4a4a;
    --ink-soft: #5c5c5c;
    --silver: #bdbdbd;
    --gold-deep: #b48c08;
    --gold-bright: #f0d11c;
  }
  * { margin: 0; padding: 0; box-sizing: border-box; }
  html, body { width: 1200px; height: 900px; overflow: hidden; background: var(--stage); }
  body { position: relative; font-family: "Arimo", Arial, sans-serif; }

  .card { position: absolute; left: 243px; width: 715px; overflow: hidden; }
  .card-front { top: 26px; height: 405px; background: var(--paper); }
  .card-back {
    top: 462px; height: 409px;
    background: linear-gradient(180deg, var(--gold-deep) 0%, #d6b011 28%, var(--gold-bright) 48%, #dcb511 72%, var(--gold-deep) 100%);
  }

  .wave { position: absolute; inset: 0; width: 715px; height: 405px; }

  .brand-seal {
    position: absolute; border-radius: 50%;
    background: var(--paper);
    display: flex; align-items: center; justify-content: center; text-align: center;
    color: var(--brand-red); font-weight: 700; line-height: 1.15;
  }
  .card-front .brand-seal {
    left: 63px; top: 22px; width: 180px; height: 180px;
    border: 3px solid var(--paper);
    box-shadow: 0 0 0 2px var(--brand-red) inset, 0 0 0 9px var(--paper) inset;
    font-size: 22px;
  }
  .card-back .brand-seal {
    left: 263px; top: 93px; width: 190px; height: 190px;
    border: 5px solid var(--brand-red);
    box-shadow: 0 0 0 4px var(--paper);
    font-size: 23px;
  }

  .person { position: absolute; left: 106px; top: 288px; }
  .person-name { font-size: 29px; color: var(--ink); letter-spacing: 0.5px; line-height: 1; }
  .person-name .first { color: var(--brand-red); font-weight: 700; }
  .person-title { font-size: 18px; color: var(--ink-soft); letter-spacing: 1.2px; margin-left: 33px; margin-top: 2px; }

  .contact { position: absolute; left: 460px; top: 0; list-style: none; }
  .contact li {
    position: absolute; left: 0; display: flex; align-items: center;
    font-size: 17px; line-height: 22px; color: var(--ink-soft); white-space: nowrap;
  }
  .contact .icon { width: 30px; height: 26px; margin-right: 11px; flex: none; }
  .contact .address { top: 201px; line-height: 31px; align-items: flex-start; }
  .contact .address .icon { height: 40px; margin-top: 4px; }
  .contact .phone-office { top: 267px; }
  .contact .phone-mobile { top: 304px; }
  .contact .email { top: 335px; }
  .contact .web { top: 366px; }

  .tagline {
    position: absolute; left: 0; right: 0; top: 289px; text-align: center;
    color: var(--paper); font-size: 16.3px; letter-spacing: 1.3px;
  }
</style>
</head>
<body>

<section class="card card-front" aria-label="Card front">
  <svg class="wave" viewBox="0 0 715 405" aria-hidden="true">
    <path fill="var(--silver)" d="M300 205 C420 125 600 112 715 152 V172 C600 135 440 140 300 205 Z"/>
    <path fill="var(--brand-red)" d="M0 0 H715 V152 C600 112 470 112 360 162 C260 210 175 248 105 224 C62 210 28 188 0 168 Z"/>
  </svg>

  <div class="brand-seal">Harbor<br>Tap Co.</div>

  <div class="person">
    <p class="person-name"><span class="first">DALE</span> VERNO</p>
    <p class="person-title">Sales Manager</p>
  </div>

  <ul class="contact">
    <li class="address">
      <svg class="icon" viewBox="0 0 30 40"><path fill="var(--brand-red)" d="M15 2 C8 2 4 7 4 12 C4 19 12 25 15 38 C18 25 26 19 26 12 C26 7 22 2 15 2 Z"/></svg>
      <span>482 Kingsley Street<br>Brooklyn, NY 11206</span>
    </li>
    <li class="phone-office">
      <svg class="icon" viewBox="0 0 30 26"><path fill="var(--brand-red)" d="M3 8 C3 3 27 3 27 8 V10 H21 V7 H9 V10 H3 Z M8 11 H22 L26 23 H4 Z"/><circle cx="15" cy="17" r="3.5" fill="var(--paper)"/></svg>
      <span>(555) 304-1180</span>
    </li>
    <li class="phone-mobile">
      <svg class="icon" viewBox="0 0 30 30"><rect x="8" y="1" width="14" height="28" rx="2.5" fill="none" stroke="var(--brand-red)" stroke-width="2.2"/><line x1="9" y1="24" x2="21" y2="24" stroke="var(--brand-red)" stroke-width="1.6"/></svg>
      <span>(555) 417-2296</span>
    </li>
    <li class="email">
      <svg class="icon" viewBox="0 0 30 22"><rect x="2" y="2" width="26" height="18" fill="none" stroke="var(--brand-red)" stroke-width="2.2"/><path d="M2 2 L15 13 L28 2 M2 20 L12 11 M28 20 L18 11" fill="none" stroke="var(--brand-red)" stroke-width="2"/></svg>
      <span>dverno@mailbox.com</span>
    </li>
    <li class="web">
      <svg class="icon" viewBox="0 0 30 30"><circle cx="15" cy="15" r="13" fill="var(--brand-red)"/><g fill="none" stroke="var(--paper)" stroke-width="1.4"><ellipse cx="15" cy="15" rx="6" ry="12"/><line x1="15" y1="3" x2="15" y2="27"/><line x1="3" y1="15" x2="27" y2="15"/><path d="M5 9 H25 M5 21 H25"/></g></svg>
      <span>www.harbortapco.com</span>
    </li>
  </ul>
</section>

<section class="card card-back" aria-label="Card back">
  <div class="brand-seal">Harbor<br>Tap Co.</div>
  <p class="tagline">Premier Craft &amp; Import Beer Distributor</p>
</section>

</body>
</html>
```